Talbek vodka

With the logo attached in the subsequent file, a business card that reflects a premium and organic vodka. On the first side, the company logo in large. The names must be included on the back of the card (Mateo Ignacio Dalmau Ferrerons with the number +34 655 219 870 and Oriol Batlle Quintana and +34 677 341 592). The slogan "What binds us" and "Organic and permium vodka" in bold E-mail (talbekvodka@mailora.net); Website www.talbekvodkaorg.net

```html
<!DOCTYPE html>
<html lang="en">
<head>
<meta charset="utf-8">
<title>Talbek Vodka — Business Card</title>
<link rel="stylesheet" href="https://fonts.googleapis.com/css2?family=EB+Garamond:wght@400;600&family=Montserrat:wght@600&display=swap">
<style>
  :root {
    --backdrop: #9b9b9b;
    --card-light: #f3f3f1;
    --card-dark: #6e6f72;
    --ink-grey: #8a8a8c;
    --ink-soft: #9c9c9e;
    --ink-white: #ffffff;
  }
  * { margin: 0; padding: 0; box-sizing: border-box; }
  html, body { width: 1200px; height: 1037px; overflow: hidden; }
  body {
    background: var(--backdrop);
    position: relative;
    font-family: "EB Garamond", Georgia, serif;
  }
  .card {
    position: absolute;
    left: 250px;
    width: 700px;
    height: 410px;
    border-radius: 4px;
    box-shadow: 0 6px 18px rgba(0,0,0,0.18);
  }
  .card--front { top: 80px; background: var(--card-light); }
  .card--back  { top: 547px; background: var(--card-dark); }

  .brand {
    position: absolute;
    right: 56px;
    top: 120px;
    display: flex;
    align-items: center;
    gap: 12px;
  }
  .brand__mark {
    width: 22px; height: 22px;
    border-radius: 50%;
    background: var(--ink-soft);
  }
  .brand__name {
    font-family: "EB Garamond", Georgia, serif;
    font-weight: 400;
    font-size: 46px;
    letter-spacing: 2px;
    color: var(--ink-soft);
    text-transform: uppercase;
  }

  .contacts {
    position: absolute;
    left: 44px;
    bottom: 42px;
    color: var(--ink-grey);
    line-height: 1.25;
  }
  .contacts__name { font-weight: 600; font-size: 22px; }
  .contacts__phone { font-size: 19px; margin-bottom: 4px; }
  .contacts__web { font-size: 18px; }
  .contacts__sep { padding: 0 6px; }

  .scene-art {
    position: absolute;
    left: 210px;
    top: 40px;
    width: 280px;
    height: 230px;
    border-radius: 50% 50% 6px 6px / 30% 30% 6px 6px;
    background: linear-gradient(180deg, rgba(255,255,255,0.55), rgba(255,255,255,0.9));
  }
  .slogan {
    position: absolute;
    left: 0; right: 0;
    top: 300px;
    text-align: center;
    font-family: "Montserrat", Arial, sans-serif;
    font-weight: 600;
    font-size: 17px;
    letter-spacing: 1px;
    line-height: 1.3;
    color: var(--ink-white);
    text-transform: uppercase;
  }
</style>
</head>
<body>
  <section class="card card--front">
    <div class="brand">
      <span class="brand__mark"></span>
      <span class="brand__name">Talbek Vodka</span>
    </div>
    <div class="contacts">
      <p class="contacts__name">Mateo Ignacio Dalmau Ferrerons</p>
      <p class="contacts__phone">+34 655 219 870</p>
      <p class="contacts__name">Oriol Batlle Quintana</p>
      <p class="contacts__phone">+34 677 341 592</p>
      <p class="contacts__web">talbekvodka@mailora.net<span class="contacts__sep">|</span>www.talbekvodkaorg.net</p>
    </div>
  </section>

  <section class="card card--back">
    <div class="scene-art" role="img" aria-label="Illustration of pine trees behind a small cabin on a curved hill"></div>
    <p class="slogan">What binds us<br>Organic &amp; Permium Vodka</p>
  </section>
</body>
</html>
```